Polling Analysis Hub Wordpress Web Design

Polling Analysis Hub, in association with The Brenlow Institute at The University of Eastwick Vale, needs a 5-page Wordpress website designed from scratch. Using the provided logos/font/color palette
We need a nicely designed site (based on the color scheme, font, and logo that we provided) that is 5 pages.
What I am thinking is:
1)Home Page - a brief breakdown of what the Polling Analysis Hub is, how it relates to the University and The Brenlow Institute
2)About - 3-4 biography sections about the employees of the PAH with headshots
3)Our Work - A page about the clients they have worked with in the past, testimonials/case studies, and maybe a scroll of logos from clients they have worked with
4)Capabilities - a breakdown of 3-4 segmented sections describing the work that they do and their ideal target markets
5)Contact Us - a contact form that we can redirect to the manager

Please use College/University and Maine stock photos as place holders. Lorem Ipsum and stock images are completely fine.
Please note that we are in the process of collecting the final text copy for the website. Designers can use text place holders for the time being. The winner will then be ask to use the final content.

Target Market(s)

University faculty, Local and regional non-profits and government agencies

Industry/Entity Type

Data analysis, Surveying, B2B, Higher Education

Coding

Coded - Design and coding required

Number of Pages Required

5+ page

Font styles to use
Serif
Sans Serif

Requirements
Must have
• footer must mention "a division of The Brenlow Institute" (logo attached).

```html
<!DOCTYPE html>
<html lang="en">
<head>
<meta charset="utf-8">
<title>Polling Analysis Hub</title>
<link href="https://fonts.googleapis.com/css2?family=Raleway:wght@300;400;500;600&family=Lato:ital,wght@0,400;0,700;1,400&display=swap" rel="stylesheet">
<style>
:root{
  --coral:#e3603f;
  --wine:#6b1d45;
  --wine-deep:#5a1539;
  --btn-dark:#8c1f35;
  --ink:#2b2b2b;
  --text:#444;
  --muted:#f1f2f4;
  --footer:#121212;
  --white:#fff;
}
*{box-sizing:border-box;margin:0;padding:0}
html,body{width:1200px;height:4396px;overflow:hidden}
body{position:relative;font-family:'Lato',sans-serif;color:var(--text);background:var(--white)}
.abs{position:absolute}
.heading{font-family:'Raleway',sans-serif;font-weight:300;text-transform:uppercase;color:var(--ink);text-align:center;font-size:40px;letter-spacing:.5px}
.rule{width:30px;height:4px;background:var(--coral);margin:8px auto 0}
.btn{display:inline-block;border-radius:22px;background:linear-gradient(90deg,var(--coral),var(--btn-dark));color:var(--white);font-family:'Raleway',sans-serif;font-size:16px;text-transform:uppercase;text-align:center;box-shadow:0 3px 6px rgba(0,0,0,.2)}
.btn-dark{background:linear-gradient(90deg,#9a2a3a,var(--wine-deep))}

/* header */
.brand{left:105px;top:8px;font-family:'Raleway',sans-serif;font-weight:500;color:var(--coral);font-size:22px;letter-spacing:3px;line-height:30px}
.brand span{display:block}
.topbar{top:10px;left:470px;font-size:12px;color:#333;display:flex;align-items:center}
.topbar div{padding:0 22px;border-right:1px solid #333;height:22px;display:flex;align-items:center;gap:6px}
.topbar div:last-child{border:none}
.dot{width:9px;height:9px;border-radius:50%;background:#333;display:inline-block}
.navbar{top:43px;left:333px;width:867px;height:42px;background:var(--wine);clip-path:polygon(40px 0,100% 0,100% 100%,0 100%)}
.nav{position:absolute;right:120px;top:0;display:flex;gap:32px;height:42px;align-items:center;font-size:13px;font-weight:700;color:var(--white);text-transform:uppercase}

/* hero */
.hero{top:85px;left:0;width:1200px;height:675px;background:linear-gradient(180deg,#7a8aa3 0%,#c9b6a0 30%,#e9b27a 45%,#6a5a52 62%,#3c3936 100%)}
.hero-box{top:260px;left:152px;width:898px;height:329px;background:rgba(70,70,70,.55);text-align:center;color:var(--white)}
.hero-box .kicker{font-family:'Raleway',sans-serif;font-size:28px;letter-spacing:10px;margin-top:42px;font-weight:300}
.hero-box h1{font-family:'Raleway',sans-serif;font-weight:300;font-size:58px;margin-top:4px;letter-spacing:1px}
.hero-box p{font-size:13.5px;line-height:25px;margin:12px 28px 0}

/* about */
.about-title{top:843px;left:0;width:1200px}
.about-logo{top:1015px;left:80px;width:460px;font-family:'Raleway',sans-serif;font-weight:500;color:var(--coral);font-size:38px;letter-spacing:3px;line-height:60px;text-align:center;white-space:nowrap}
.about-text{top:925px;left:602px;width:463px;font-size:13px;line-height:26.5px;text-align:justify}

/* capabilities */
.caps{top:1360px;left:0;width:1200px;height:688px;background:var(--muted)}
.card{width:300px;height:375px;background:var(--white);border-radius:10px;box-shadow:0 2px 10px rgba(0,0,0,.15);top:1545px;text-align:center}
.card .photo{margin:6px;height:195px;border-radius:8px}
.card h3{font-family:'Raleway',sans-serif;font-weight:400;font-size:16px;color:var(--coral);text-transform:uppercase;margin-top:16px}
.card p{font-size:12px;line-height:24px;padding:4px 18px 0;color:#333}
.card .btn{position:absolute;left:72px;bottom:-25px;width:172px;height:50px;line-height:50px}

/* work */
.work{top:2048px;left:0;width:1200px;height:589px;background:linear-gradient(90deg,#6a1c44,#72204b,#6a1c44)}
.avatar{border-radius:50%;border:3px solid var(--white);background:linear-gradient(160deg,#b9a59a,#5c4a45)}
.quote{top:2356px;left:180px;width:840px;color:var(--white);font-style:italic;font-size:13px;line-height:26.5px;text-align:center}
.quote-name{top:2530px;left:0;width:1200px;text-align:center;color:var(--white);font-size:13px}
.quote-name b{font-size:18px;font-weight:700}

/* how it works */
.diamond-label{font-size:12.5px;font-weight:700;color:#333;text-align:center;text-transform:uppercase;line-height:19px;width:170px}

/* contact */
.contact{top:3291px;left:0;width:1200px;height:692px;background:linear-gradient(135deg,#e6e3e1,#f2f0ee 40%,#dcd6d2 70%,#ebe8e6)}
.field{background:var(--white);border:1px solid #ddd;font-size:12px;color:#666;padding:0 20px;display:flex;align-items:center}

/* footer */
.footer{top:3983px;left:0;width:1200px;height:413px;background:var(--footer);color:var(--white)}
.ft-head{font-size:15px;text-transform:uppercase;font-weight:400;color:var(--white)}
.ft-list{font-size:13px;line-height:28px;color:var(--white)}
.ft-text{color:var(--white)}
.social{width:28px;height:28px;border-radius:50%;background:var(--wine)}
.ic{width:26px;height:26px;border-radius:50%;background:var(--wine);display:flex;align-items:center;justify-content:center}
</style>
</head>
<body>

<!-- header -->
<div class="abs brand"><span>POLLING ANALYSIS</span><span style="font-size:15px;letter-spacing:6px">HUB</span></div>
<div class="abs topbar">
  <div>
    <svg width="11" height="11" viewBox="0 0 24 24"><path d="M6 2l4 5-3 3c1 3 4 6 7 7l3-3 5 4-3 4C10 22 2 14 2 5z" fill="#333"/></svg>
    +1 555 014 2290
  </div>
  <div>
    <svg width="12" height="10" viewBox="0 0 24 18"><rect x="1" y="1" width="22" height="16" fill="none" stroke="#333" stroke-width="2"/><path d="M1 1l11 9 11-9" fill="none" stroke="#333" stroke-width="2"/></svg>
    hello@pollinganalysishub.org
  </div>
  <div>
    <svg width="11" height="11" viewBox="0 0 24 24"><path d="M2 10h12l-4-4 2-2 8 8-8 8-2-2 4-4H2z" fill="#333"/></svg>
    Login
  </div>
  <div><span class="dot"></span><span class="dot"></span><span class="dot"></span><span class="dot"></span></div>
</div>
<div class="abs navbar">
  <nav class="nav"><span>Home</span><span>About Us</span><span>Our Work</span><span>Capabilities</span><span>Contact Us</span></nav>
</div>

<!-- hero -->
<div class="abs hero" role="img" aria-label="Photo of a coastal lighthouse on rocky cliffs at sunset"></div>
<div class="abs hero-box">
  <div class="kicker">WELCOME TO</div>
  <h1>POLLING ANALYSIS HUB</h1>
  <p>Lorem ipsum dolor sit amet, consectetur adipiscing elit, sed do eiusmod tempor incididunt ut labore et dolore magna aliqua. Quis ipsum suspendisse ultrices gravida. Risus commodo viverra maecenas accumsan lacus vel facilisis.</p>
  <span class="btn" style="width:146px;height:38px;line-height:38px;margin-top:14px;font-size:15px">Get Started</span>
</div>

<!-- about -->
<div class="abs about-title"><h2 class="heading">What the Polling Analysis Hub</h2><div class="rule"></div></div>
<div class="abs about-logo">POLLING ANALYSIS<br><span style="font-size:30px;letter-spacing:8px">HUB</span></div>
<p class="abs about-text">Lorem ipsum dolor sit amet, consectetur adipiscing elit, sed do eiusmod tempor incididunt ut labore et dolore magna aliqua. Ut enim ad minim veniam, quis nostrud exercitation ullamco laboris nisi ut aliquip ex ea commodo consequat. Duis aute irure dolor in reprehenderit in voluptate velit esse cillum dolorenatus error sit voluptatem accusantium doloremque laudantium, totam rem aperiam, eaque ipsa quae ab illo inventore veritatis et quasi architecto beatae vitae dicta sunt explicabo. Nemo enim ipsam voluptatem quia voluptas sit aspernatur aut odit aut fugit, sed quia consequuntur magni dolores eos qui ratione voluptatem sequi nesciunt Neque porro quisquam est, qui dolorem ipsum.voluptas sit aspernatur aut odit aut fugit sed quia consequuntur magni dolores.</p>
<span class="abs btn" style="top:1220px;left:602px;width:146px;height:42px;line-height:42px">Learn More</span>

<!-- capabilities -->
<div class="abs caps"></div>
<div class="abs" style="top:1450px;left:0;width:1200px"><h2 class="heading">Capabilities</h2><div class="rule"></div></div>
<div class="abs card" style="left:131px">
  <div class="photo" role="img" aria-label="Photo of students studying together at a library table" style="background:linear-gradient(150deg,#6b4a36,#b08868 55%,#c94a3e)"></div>
  <h3>Lorem Ipsum Dolor</h3>
  <p>Based on the Regional Learning Standards and the Shared Primary Framework, PAH will meet and exceed the educational needs of all students in our care.</p>
  <span class="btn btn-dark">Learn More</span>
</div>
<div class="abs card" style="left:449px">
  <div class="photo" role="img" aria-label="Photo of a group of college students walking in a hallway" style="background:linear-gradient(150deg,#8a7258,#c9b79a 50%,#4d5e80)"></div>
  <h3>Lorem Ipsum Dolor</h3>
  <p>Based on the Regional Learning Standards and the Shared Primary Framework, PAH will meet and exceed the educational needs of all students in our care.</p>
  <span class="btn btn-dark">Learn More</span>
</div>
<div class="abs card" style="left:768px">
  <div class="photo" role="img" aria-label="Photo of a university lecture hall filled with students" style="background:linear-gradient(150deg,#8c6a3a,#d9c4a0 55%,#6e5b48)"></div>
  <h3>Lorem Ipsum Dolor</h3>
  <p>Based on the Regional Learning Standards and the Shared Primary Framework, PAH will meet and exceed the educational needs of all students in our care.</p>
  <span class="btn btn-dark">Learn More</span>
</div>

<!-- our work -->
<div class="abs work" role="img" aria-label="Faded photo of students on campus under a wine tint"></div>
<div class="abs" style="top:2106px;left:0;width:1200px"><h2 class="heading" style="color:var(--white)">Our Work</h2><div class="rule" style="background:var(--white)"></div></div>
<div class="abs avatar" role="img" aria-label="Client headshot" style="top:2240px;left:457px;width:76px;height:76px"></div>
<div class="abs avatar" role="img" aria-label="Client headshot" style="top:2227px;left:548px;width:104px;height:104px"></div>
<div class="abs avatar" role="img" aria-label="Client headshot" style="top:2240px;left:666px;width:76px;height:76px"></div>
<svg class="abs" style="top:2390px;left:86px" width="22" height="20" viewBox="0 0 22 20"><path d="M21 10H3M10 2L2 10l8 8" fill="none" stroke="#fff" stroke-width="2.5"/></svg>
<svg class="abs" style="top:2390px;left:1092px" width="22" height="20" viewBox="0 0 22 20"><path d="M1 10h18M12 2l8 8-8 8" fill="none" stroke="#fff" stroke-width="2.5"/></svg>
<p class="abs quote">Lorem ipsum dolor sit amet, consectetur adipiscing elit, sed do eiusmod tempor incididunt ut labore et dolore magna aliqua. Quis ipsum suspendisse ultrices gravida. Risus commodo viverra maecenas accumsan lacus vel facilisis. ut perspiciatis unde omnis iste natus error sit voluptatem accusantium doloremque laudantium, totam rem aperiam, eaque ipsa quae ab illo inventore veritatis et quasi architecto beatae vitae dicta sunt explicabo. Nemo enim ipsam voluptatem quia voluptas sit aspernatur aut odit aut fugit, sed quia consequuntur magni dolores eos qui ratione voluptatem sequi nesciunt. Neque porro quisquam est, qui dolorem ipsum quia dolor sit amet, consectetur, adipisci velit, sed quia non numquam eius modi tempora</p>
<div class="abs quote-name"><b>Dana Whitcomb</b> - Lorem ipsum dolor sit</div>

<!-- how it works -->
<div class="abs" style="top:2720px;left:0;width:1200px"><h2 class="heading">How It Works</h2><div class="rule"></div></div>
<svg class="abs" style="top:2800px;left:200px" width="800" height="400" viewBox="200 2800 800 400">
  <g fill="#fff" stroke="#e3603f" stroke-width="3" stroke-linejoin="round">
    <rect x="248" y="2856" width="160" height="160" rx="22" transform="rotate(45 328 2936)"/>
    <rect x="521" y="2856" width="160" height="160" rx="22" transform="rotate(45 601 2936)"/>
    <rect x="791" y="2856" width="160" height="160" rx="22" transform="rotate(45 871 2936)"/>
    <rect x="383" y="2993" width="160" height="160" rx="22" transform="rotate(45 463 3073)"/>
    <rect x="656" y="2993" width="160" height="160" rx="22" transform="rotate(45 736 3073)"/>
  </g>
  <g fill="none" stroke="#e3603f" stroke-width="2.5">
    <path d="M392 3020l18 18M410 3026v12h-12"/>
    <path d="M530 3050l-18-18M512 3044v-12h12"/>
    <path d="M665 3020l18 18M683 3026v12h-12"/>
    <path d="M800 3050l-18-18M800 3044v-12h12"/>
  </g>
  <g fill="none" stroke="#5a1539" stroke-width="2">
    <rect x="298" y="2880" width="36" height="24" rx="2"/><rect x="314" y="2894" width="34" height="22" rx="2"/>
    <path d="M320 2902h22M320 2908h22"/>
    <rect x="580" y="2885" width="44" height="34" rx="2"/><path d="M580 2893h44M588 2902h16M588 2909h26"/>
    <path d="M852 2910l20-24 4 8 8-4M850 2914l10-2" stroke-width="2.5"/><circle cx="866" cy="2880" r="4"/>
    <path d="M448 3025l12-16 8 6-10 16zM456 3034q6 10 20 4"/>
    <rect x="714" y="3012" width="44" height="20" rx="2"/><path d="M722 3012v20M750 3012v20M736 3032v10"/><circle cx="730" cy="3046" r="4"/><circle cx="742" cy="3046" r="4"/>
  </g>
</svg>
<div class="abs diamond-label" style="top:2930px;left:243px">Lorem ipsum dolor sit amet, consectetur adipiscing elit</div>
<div class="abs diamond-label" style="top:2935px;left:516px">Lorem ipsum dolor sit amet, consectetur adipiscing elit</div>
<div class="abs diamond-label" style="top:2935px;left:786px">Lorem ipsum dolor sit amet, consectetur adipiscing elit</div>
<div class="abs diamond-label" style="top:3072px;left:378px">Lorem ipsum dolor sit amet consectetur adipiscing elit</div>
<div class="abs diamond-label" style="top:3070px;left:651px">Lorem ipsum dolor sit amet, consectetur adipiscing elit</div>

<!-- get in touch -->
<div class="abs contact" role="img" aria-label="Faded photo of students studying in a classroom"></div>
<div class="abs" style="top:3368px;left:0;width:1200px"><h2 class="heading">Get In Touch</h2><div class="rule"></div></div>
<div class="abs field" style="top:3470px;left:300px;width:292px;height:46px">First Name</div>
<div class="abs field" style="top:3470px;left:607px;width:293px;height:46px">Last Name</div>
<div class="abs field" style="top:3535px;left:300px;width:600px;height:46px">Email Address</div>
<div class="abs field" style="top:3598px;left:300px;width:292px;height:47px">Phone Number</div>
<div class="abs field" style="top:3598px;left:607px;width:293px;height:47px">Subject</div>
<div class="abs field" style="top:3667px;left:300px;width:600px;height:118px;align-items:flex-start;padding-top:18px">Message</div>
<span class="abs btn btn-dark" style="top:3846px;left:514px;width:172px;height:50px;line-height:50px">Submit</span>

<!-- footer -->
<div class="abs footer"></div>
<div class="abs" style="top:4092px;left:110px;width:250px;text-align:center;font-family:'Raleway',sans-serif;font-weight:500;color:var(--white);font-size:20px;letter-spacing:1px;line-height:30px;white-space:nowrap">POLLING ANALYSIS<br><span style="font-size:15px;letter-spacing:6px">HUB</span></div>
<div class="abs social" style="top:4199px;left:157px"></div>
<div class="abs social" style="top:4199px;left:201px"></div>
<div class="abs social" style="top:4199px;left:245px"></div>
<div class="abs social" style="top:4199px;left:290px"></div>

<div class="abs" style="top:4058px;left:394px">
  <div class="ft-head">Quick Links</div>
  <div class="ft-list" style="margin-top:6px">
    <div>»&nbsp;&nbsp;&nbsp;Home</div><div>»&nbsp;&nbsp;&nbsp;About Us</div><div>»&nbsp;&nbsp;&nbsp;Our Work</div><div>»&nbsp;&nbsp;&nbsp;Capabilities</div><div>»&nbsp;&nbsp;&nbsp;Contact us</div>
  </div>
</div>

<div class="abs ft-text" style="top:4058px;left:550px;width:240px">
  <div class="ft-head">Contact Us</div>
  <div class="abs ic" style="top:38px;left:0"><svg width="12" height="14" viewBox="0 0 12 16"><path d="M6 0a6 6 0 0 1 6 6c0 4-6 10-6 10S0 10 0 6a6 6 0 0 1 6-6z" fill="#fff"/><circle cx="6" cy="6" r="2" fill="#6b1d45"/></svg></div>
  <div class="abs" style="top:38px;left:42px;width:200px;font-size:13px;line-height:28px">123 Lorem ipsum dolor sit amet consectetur adipiscing elit sed do eiusmod tempor.</div>
  <div class="abs ic" style="top:135px;left:0"><svg width="12" height="12" viewBox="0 0 24 24"><path d="M6 2l4 5-3 3c1 3 4 6 7 7l3-3 5 4-3 4C10 22 2 14 2 5z" fill="#fff"/></svg></div>
  <div class="abs" style="top:137px;left:42px;font-size:13px">+1 555 014 2290</div>
  <div class="abs ic" style="top:190px;left:0"><svg width="13" height="10" viewBox="0 0 24 18"><rect x="1" y="1" width="22" height="16" fill="#fff"/><path d="M1 1l11 9 11-9" fill="none" stroke="#6b1d45" stroke-width="2"/></svg></div>
  <div class="abs" style="top:192px;left:42px;font-size:13px">hello@pollinganalysishub.org</div>
</div>

<div class="abs ft-text" style="top:4058px;left:809px;width:270px">
  <div class="ft-head">Sign up for our newsletter</div>
  <p style="font-size:13px;line-height:28px;margin-top:6px;padding-left:8px">Lorem ipsum dolor sit amet, consectet ur adipiscing elit, sed do.</p>
</div>
<div class="abs field" style="top:4153px;left:818px;width:199px;height:38px;border:none;font-size:11px;color:#999;padding:0 12px">Enter The Email</div>
<div class="abs" style="top:4153px;left:1017px;width:53px;height:38px;background:var(--wine);display:flex;align-items:center;justify-content:center">
  <svg width="16" height="16" viewBox="0 0 24 24"><path d="M2 11L22 2l-7 20-4-8z" fill="#fff"/></svg>
</div>
<div class="abs" style="top:4222px;left:820px;width:190px;text-align:center;font-size:13px;color:var(--white)">
  <div style="font-size:11px;margin-bottom:4px">a division of</div>
  <div style="font-size:20px;letter-spacing:1px;text-transform:uppercase;white-space:nowrap">Brenlow Institute</div>
</div>

<div class="abs" style="top:4315px;left:120px;width:960px;height:1px;background:#555"></div>
<div class="abs" style="top:4345px;left:0;width:1200px;text-align:center;font-size:12px;color:var(--white)">© Copyrights 2022&nbsp; Polling Analysis Hub &nbsp;|&nbsp;&nbsp; All Rights Reserved</div>

</body>
</html>
```